Creation of a book cover
Size : 14 x 20,5 cm (+ 5 mm bleed area at the top, bottom and right areas)
The Title is a French sentence which means “The heron dreaming on the cold roof of this empty station”. It’s a surrealistic title which has no link to the story.
AUTHOR : Mathieu Vorlange
TITLE : "Le héron rêvant sur le toit froid de cette gare vide »
PUBLISHER (AT THE BOTTOM OF THE PAGE) : Editions Parvenche
I send a PDF file with the kind of cover we have imagine, but you can propose something different. The glass and the fly can of course be used.

```html
<!DOCTYPE html>
<html lang="fr">
<head>
<meta charset="utf-8">
<title>Le héron rêvant sur le toit froid de cette gare vide — Couverture</title>
<link rel="stylesheet" href="https://fonts.googleapis.com/css2?family=Open+Sans:ital,wght@0,300;0,400;0,600;0,700;1,300;1,400&family=Tinos:wght@700&family=Arimo:wght@400&display=swap">
<style>
  :root {
    --page-bg: #ffffff;
    --back-cover: #e4d5b2;
    --spine: #eadbb8;
    --front-cover: #f4e7c8;
    --ink: #1a1a1a;
    --ink-soft: #2a2a2a;
    --placeholder: #e6e6e6;
    --isbn-text: #8a8a8a;
    --band: #8d9f99;
    --art-light: #eef0ea;
    --art-mid: #9fb2b3;
    --art-dark: #40565c;
  }
  * { margin: 0; padding: 0; box-sizing: border-box; }
  html, body {
    width: 1200px; height: 960px; overflow: hidden;
    background: var(--page-bg);
  }
  .spread {
    position: absolute; left: 40px; top: 84px;
    width: 1120px; height: 793px;
    display: flex;
  }
  .back-cover {
    position: relative; width: 518px; height: 100%;
    background: var(--back-cover);
    font-family: "Arimo", Arial, sans-serif;
    color: var(--ink-soft);
  }
  .back-heading {
    position: absolute; left: 49px; top: 64px;
    font-family: "Open Sans", sans-serif;
    font-weight: 700; font-size: 18px; letter-spacing: 0.2em;
    color: var(--ink);
  }
  .back-heading-sub {
    position: absolute; left: 49px; top: 88px;
    font-family: "Open Sans", sans-serif;
    font-style: italic; font-weight: 400; font-size: 17px;
    color: var(--ink);
  }
  .author-photo {
    position: absolute; left: 42px; top: 125px;
    width: 110px; height: 139px;
    background: var(--placeholder);
  }
  .blurb {
    font-size: 11px; line-height: 15.2px; text-align: justify;
    hyphens: auto;
  }
  .blurb-lead {
    position: absolute; left: 173px; top: 154px; width: 302px;
  }
  .blurb-body {
    position: absolute; left: 32px; top: 278px; width: 450px;
  }
  .blurb-body p + p { margin-top: 15px; }
  .blurb-body .closing { text-align: left; }
  .isbn-box {
    position: absolute; left: 29px; top: 689px;
    width: 170px; height: 86px;
    background: var(--placeholder);
    display: flex; align-items: center; justify-content: center;
    font-family: "Open Sans", sans-serif; font-weight: 300;
    font-size: 26px; letter-spacing: 0.22em; color: var(--isbn-text);
  }
  .back-imprint {
    position: absolute; left: 214px; top: 728px;
    font-family: "Open Sans", sans-serif; color: var(--ink);
    letter-spacing: 0.16em; line-height: 24px;
  }
  .back-imprint .publisher { font-weight: 400; font-size: 15px; }
  .back-imprint .author { font-weight: 600; font-size: 15px; }

  .spine {
    position: relative; width: 84px; height: 100%;
    background: var(--spine);
  }
  .spine-text {
    position: absolute; left: 50%; top: 16px;
    transform: translateX(-50%);
    writing-mode: vertical-rl;
    font-family: "Open Sans", sans-serif; color: var(--ink);
    white-space: nowrap;
  }
  .spine-title { font-weight: 400; font-size: 21px; letter-spacing: 0.02em; }
  .spine-divider { font-size: 21px; margin: 4px 0; }
  .spine-publisher { font-weight: 400; font-size: 16px; letter-spacing: 0.3em; }

  .front-cover {
    position: relative; width: 518px; height: 100%;
    background: var(--front-cover);
    color: var(--ink);
    text-align: center;
  }
  .front-author {
    position: absolute; left: 0; right: 0; top: 30px;
    font-family: "Open Sans", sans-serif; font-weight: 600;
    font-size: 21px; letter-spacing: 0.2em;
  }
  .front-title {
    position: absolute; left: 0; right: 0; top: 134px;
    font-family: "Tinos", "Times New Roman", serif; font-weight: 700;
    font-size: 64px; line-height: 1; letter-spacing: 0.01em;
  }
  .front-subtitle {
    position: absolute; left: 0; right: 0; top: 218px;
    font-family: "Open Sans", sans-serif; font-style: italic; font-weight: 300;
    font-size: 21px; line-height: 33px;
  }
  .cover-art {
    position: absolute; left: 115px; top: 390px;
    width: 265px; height: 296px;
    border-radius: 8px;
    background: radial-gradient(ellipse at 55% 60%, var(--art-mid) 0%, var(--art-light) 70%, var(--front-cover) 100%);
  }
  .publisher-band {
    position: absolute; left: 0; right: 0; top: 737px; height: 31px;
    background: var(--band);
    display: flex; align-items: center; justify-content: center;
    font-family: "Open Sans", sans-serif; font-weight: 400;
    font-size: 15px; letter-spacing: 0.22em; color: var(--ink);
  }
</style>
</head>
<body>
  <main class="spread">
    <section class="back-cover">
      <h2 class="back-heading">TEXTE DE QUATRIÈME</h2>
      <p class="back-heading-sub">de couverture (en français)</p>
      <div class="author-photo"></div>
      <p class="blurb blurb-lead">Dans ce récit délicat et profondément original, Mathieu Vorlange nous invite à porter un regard neuf sur l’insignifiant, à travers la contemplation d’un simple verre d’eau et d’une mouche qui s’y pose. Mais ce qui semble au premier abord anodin devient, sous sa plume, une porte ouverte vers une réflexion plus vaste sur la vie, le temps, et notre place dans le monde.</p>
      <div class="blurb blurb-body">
        <p>Avec une élégance ironique et un sens aigu de l’observation, l’auteur tisse une fable contemporaine où chaque détail révèle un sens caché. Les gestes les plus quotidiens prennent une résonance inattendue, les silences deviennent parole, et l’absurde se fait révélateur de vérités profondes.</p>
        <p>Ce livre raconte l’histoire d’un homme ordinaire, témoin silencieux d’une scène simple mais chargée de mystère. Tandis qu’il observe la mouche et son rituel inattendu, il se surprend à devenir lui-même l’objet d’un regard. Entre humour subtil, tendresse pour la condition humaine et clins d’œil littéraires, Mathieu Vorlange déploie un univers où le réel et l’imaginaire se confondent.</p>
        <p class="closing">« Observer, c’est déjà changer le monde. »<br>Ce roman est une invitation à ralentir, à s’émerveiller, et à retrouver cette capacité à voir l’invisible dans l’ordinaire.</p>
        <p class="closing">Alors, êtes-vous prêts à voir la mouche autrement ?<br>Et surtout, à découvrir ce qu’elle peut vous apprendre sur vous-même ?</p>
      </div>
      <div class="isbn-box">ISBN</div>
      <div class="back-imprint">
        <div class="publisher">ÉDITIONS PARVENCHE</div>
        <div class="author">MATHIEU VORLANGE</div>
      </div>
    </section>

    <section class="spine">
      <div class="spine-text">
        <span class="spine-title">LE HÉRON</span><span class="spine-divider">|</span><span class="spine-publisher">ÉDITIONS PARVENCHE</span>
      </div>
    </section>

    <section class="front-cover">
      <p class="front-author">MATHIEU VORLANGE</p>
      <h1 class="front-title">LE HÉRON</h1>
      <p class="front-subtitle">RÊVANT SUR LE TOIT FROID<br>DE CETTE GARE VIDE</p>
      <div class="cover-art" role="img" aria-label="Illustration : une mouche posée sur le bord d’un verre d’eau"></div>
      <div class="publisher-band">ÉDITIONS PARVENCHE</div>
    </section>
  </main>
</body>
</html>
```